2 Creative Website Banners for Furniture Brand

Morning Tobrasca....
The get a great night sleep banner is complete - we are happy with that one.
Ive uploaded a slightly different concept for the other banner below. This is just something rough ive thrown together. But you can see I have added a curve, a maroon coloured background which is slightly transparent and a big heart in the background....
I do not necessarily want to use this heart image but something a bit like this (a nice graphic, gif etc) but something quite elegant faded in, or perhaps a number of hearts (done in a tasteful way). Also can we keep the typography in the same format as you can see for this one.
Nearly there :)!
Industry/Entity Type
Furniture

```html
<!DOCTYPE html>
<html lang="en">
<head>
<meta charset="utf-8">
<title>Find a Look You Love – Harlowe Furniture</title>
<link href="https://fonts.googleapis.com/css2?family=Raleway:wght@400;500;700&family=Cormorant+Garamond:wght@600&family=Crimson+Text:wght@400&display=swap" rel="stylesheet">
<style>
  :root {
    --plum: #34162f;
    --gold: #c49a6c;
    --ink-light: #ffffff;
    --room-deep: #141214;
    --room-shadow: #262326;
    --room-mid: #47424a;
    --room-soft: #6c666a;
    --room-warm: #5a5048;
  }
  * { margin: 0; padding: 0; box-sizing: border-box; }
  html, body {
    width: 1200px;
    height: 356px;
    overflow: hidden;
    background: var(--plum);
  }
  .banner {
    position: relative;
    width: 1200px;
    height: 356px;
    background: var(--plum);
    overflow: hidden;
  }
  .banner__shape {
    position: absolute;
    inset: 0;
  }
  .banner__copy {
    position: absolute;
    left: 165px;
    top: 71px;
    width: 320px;
    text-align: center;
    color: var(--ink-light);
  }
  .banner__eyebrow {
    font-family: "Raleway", sans-serif;
    font-weight: 500;
    font-size: 23px;
    letter-spacing: 4.6px;
    margin-right: -4.6px;
    line-height: 1;
  }
  .banner__headline {
    margin-top: 16px;
    font-family: "Cormorant Garamond", serif;
    font-weight: 600;
    font-size: 80px;
    letter-spacing: 20px;
    margin-right: -20px;
    line-height: 0.8;
  }
  .banner__text {
    margin-top: 20px;
    font-family: "Crimson Text", serif;
    font-size: 17.5px;
    line-height: 20px;
  }
  .banner__button {
    display: inline-block;
    margin-top: 26px;
    width: 188px;
    height: 32px;
    line-height: 32px;
    border-radius: 16px;
    background: var(--gold);
    color: var(--plum);
    font-family: "Raleway", sans-serif;
    font-weight: 700;
    font-size: 13px;
    letter-spacing: 1.7px;
    text-decoration: none;
  }
  .banner__brand {
    position: absolute;
    left: 729px;
    width: 346px;
    top: 150px;
    text-align: center;
    color: var(--ink-light);
    font-family: "Raleway", sans-serif;
    font-weight: 400;
    line-height: 1;
  }
  .banner__brand-name {
    display: block;
    font-size: 44px;
    letter-spacing: 4px;
    margin-right: -4px;
  }
  .banner__brand-sub {
    display: block;
    margin-top: 6px;
    font-size: 14px;
    letter-spacing: 2px;
    margin-right: -2px;
  }
</style>
</head>
<body>
  <section class="banner">
    <svg class="banner__shape" width="1200" height="356" viewBox="0 0 1200 356">
      <defs>
        <linearGradient id="room-base" x1="0" y1="0" x2="1" y2="1">
          <stop offset="0" stop-color="var(--room-shadow)"/>
          <stop offset="0.5" stop-color="var(--room-mid)"/>
          <stop offset="1" stop-color="var(--room-deep)"/>
        </linearGradient>
        <radialGradient id="room-bed-glow" cx="0.45" cy="0.72" r="0.45">
          <stop offset="0" stop-color="var(--room-soft)" stop-opacity="0.9"/>
          <stop offset="1" stop-color="var(--room-soft)" stop-opacity="0"/>
        </radialGradient>
        <radialGradient id="room-lamp-glow" cx="0.42" cy="0.32" r="0.18">
          <stop offset="0" stop-color="var(--room-warm)" stop-opacity="0.8"/>
          <stop offset="1" stop-color="var(--room-warm)" stop-opacity="0"/>
        </radialGradient>
        <linearGradient id="room-edge" x1="0" y1="0" x2="1" y2="0">
          <stop offset="0.75" stop-color="var(--room-deep)" stop-opacity="0"/>
          <stop offset="1" stop-color="var(--room-deep)" stop-opacity="0.85"/>
        </linearGradient>
      </defs>
      <polygon class="banner__frame" points="729,0 1200,0 1200,356 676,356 552,165" fill="var(--gold)"/>
      <g class="banner__photo" role="img" aria-label="Dark bedroom with a grey upholstered bed, soft throw, mirrored bedside tables and a glass table lamp">
        <polygon points="735,0 1200,0 1200,356 683,356 559,165" fill="url(#room-base)"/>
        <polygon points="735,0 1200,0 1200,356 683,356 559,165" fill="url(#room-bed-glow)"/>
        <polygon points="735,0 1200,0 1200,356 683,356 559,165" fill="url(#room-lamp-glow)"/>
        <polygon points="735,0 1200,0 1200,356 683,356 559,165" fill="url(#room-edge)"/>
      </g>
    </svg>

    <div class="banner__copy">
      <p class="banner__eyebrow">FIND A LOOK YOU</p>
      <h1 class="banner__headline">LOVE</h1>
      <p class="banner__text">Lorem ipsum not sure what the rest of<br>this will say at the moment</p>
      <a class="banner__button" href="#">SHOPE BEDROOMS</a>
    </div>

    <p class="banner__brand">
      <span class="banner__brand-name">HARLOWE</span>
      <span class="banner__brand-sub">FURNITURE</span>
    </p>
  </section>
</body>
</html>
```